Building showcase catalogue for a post frame construction company

We are looking for a brochure for our clients showcasing our buildings. We are a post frame building company that makes commercial, ag, homes, and other building types. We are looking for a brochure that we can use with all the types of buildings simply by changing out the pictures. We would like a more photo heavy brochure thats 1-5 pages. We want the design to feel high end luxury. Our colors are black, white, and chrome. I will upload our logo as well as some building photos in the suburban category of our buildings. We would like a page to showcase some building layouts as well.

We need the size to be us letter size.

Industry/Entity Type

Construction

Font styles to use
Serif

Colors

Designer to choose only greyscale colors for use in the design.

Requirements
Must have
• A space to showcase building photos, small text space for information. An area to showcase building layouts.
Nice to have
• I would like to have a very clean professional look thats looks high end.
Should not have
• Areas for detail pictures. We mostly have exterior building shots.

```html
<!DOCTYPE html>
<html lang="en">
<head>
<meta charset="utf-8">
<title>Building Showcase Brochure – Inside Spread</title>
<link rel="stylesheet" href="https://fonts.googleapis.com/css2?family=Open+Sans:wght@400;800&display=swap">
<style>
  :root {
    --backdrop: #d8d8db;
    --paper: #f4f4f4;
    --paper-white: #fbfbfb;
    --ink: #111111;
    --ink-soft: #2a2a2a;
    --chrome-dark: #3a3a3a;
    --chrome-mid: #8a8a8a;
    --chrome-light: #b9b9b9;
    --text-light: #f2f2f2;
  }
  * { margin: 0; padding: 0; box-sizing: border-box; }
  html, body {
    width: 1200px; height: 840px; overflow: hidden;
    background: var(--backdrop);
    font-family: "Open Sans", Arial, sans-serif;
  }
  .spread {
    position: absolute; left: 40px; top: 58px;
    width: 1120px; height: 724px;
    display: flex;
    box-shadow: 0 10px 30px rgba(0,0,0,.18);
  }
  .page { position: relative; width: 560px; height: 724px; overflow: hidden; }
  .page svg { position: absolute; inset: 0; display: block; }
  .body-copy {
    position: absolute;
    font-size: 10.5px; line-height: 1.38;
    text-align: justify; color: var(--ink-soft);
  }
  .page-left .body-copy { left: 335px; top: 318px; width: 195px; }
  .about-title {
    position: absolute; left: 60px; top: 306px;
    font-weight: 800; font-size: 34px; line-height: 1.2; color: var(--ink);
    letter-spacing: -0.3px;
  }
  .about-copy { left: 62px; top: 352px; width: 215px; }
  .reverse-copy { left: 318px; top: 462px; width: 200px; color: var(--text-light); }
</style>
</head>
<body>
<div class="spread">

  <section class="page page-left">
    <svg viewBox="0 0 560 724" width="560" height="724">
      <defs>
        <linearGradient id="utvTone" x1="0" y1="0" x2="1" y2="1">
          <stop offset="0" stop-color="#c9c9c4"/><stop offset=".55" stop-color="#5a4e4c"/><stop offset="1" stop-color="#8f8f8c"/>
        </linearGradient>
        <linearGradient id="whiteBuildingTone" x1="0" y1="0" x2="0" y2="1">
          <stop offset="0" stop-color="#cdd8e4"/><stop offset=".6" stop-color="#e6e8ea"/><stop offset="1" stop-color="#9a8e7e"/>
        </linearGradient>
        <linearGradient id="redWallTone" x1="0" y1="0" x2="1" y2="1">
          <stop offset="0" stop-color="#c23346"/><stop offset=".7" stop-color="#d4394e"/><stop offset="1" stop-color="#6d7a55"/>
        </linearGradient>
      </defs>
      <rect class="page-bg" width="560" height="724" fill="var(--paper)"/>

      <polygon class="corner-band-dark" points="0,0 300,0 150,150 0,70" fill="var(--ink-soft)"/>
      <polygon class="corner-band-mid" points="0,70 150,150 130,185 0,120" fill="var(--chrome-mid)"/>
      <polygon class="corner-band-dark" points="150,150 170,165 140,200 130,185" fill="var(--chrome-dark)"/>

      <circle cx="300" cy="150" r="156" fill="var(--chrome-mid)"/>
      <circle cx="300" cy="150" r="140" fill="var(--paper-white)"/>
      <circle class="photo" cx="300" cy="150" r="134" fill="url(#utvTone)" role="img" aria-label="Photo of a utility vehicle parked inside a building"/>

      <circle cx="95" cy="365" r="190" fill="var(--ink)"/>
      <circle cx="95" cy="365" r="168" fill="var(--paper)"/>
      <circle class="photo" cx="95" cy="365" r="160" fill="url(#whiteBuildingTone)" role="img" aria-label="Photo of a white post frame building exterior"/>

      <polygon class="corner-band-mid" points="0,724 0,600 60,560 160,520 230,560 120,650 170,724" fill="var(--chrome-mid)"/>
      <polygon class="corner-band-light" points="60,660 120,650 170,724 100,724" fill="var(--chrome-light)"/>
      <polygon class="corner-band-dark" points="160,520 250,540 300,580 230,560" fill="var(--ink-soft)"/>

      <circle class="photo" cx="480" cy="740" r="120" fill="url(#redWallTone)" role="img" aria-label="Photo of a red building wall with a door and flowering shrubs"/>
    </svg>
    <p class="body-copy">Lorem Lorem ipsum dolor sit amet, consectetuer adipiscing elit, sed diam nonummy nibh euismod tincidunt ut laoreet dolore magna aliquam erat volutpat. Ut wisi enim ad minim veniam, quis nostrud exerci tation Lorem ipsum dolor sit amet, consectetuer adipiscing elit, sed diam nonummy nibh euismod tincidunt ut laoreet dolore magna aliquam erat volutpat. Ut wisi enim ad minim veniam, quis nostrud exerci Lorem ipsum dolor sit amet, consectetuer adipiscing elit, sed diam nonummy nibh euismod tincidunt ut laoreet dolore magna</p>
  </section>

  <section class="page page-right">
    <svg viewBox="0 0 560 724" width="560" height="724">
      <defs>
        <linearGradient id="barnTone" x1="0" y1="0" x2="0" y2="1">
          <stop offset="0" stop-color="#3f4654"/><stop offset=".3" stop-color="#8e2230"/><stop offset=".65" stop-color="#6b1e28"/><stop offset="1" stop-color="#4f6b3a"/>
        </linearGradient>
        <linearGradient id="interiorTone" x1="0" y1="0" x2="1" y2="1">
          <stop offset="0" stop-color="#6e4a2e"/><stop offset=".5" stop-color="#a06a3c"/><stop offset="1" stop-color="#4a2e22"/>
        </linearGradient>
      </defs>
      <rect class="page-bg" width="560" height="724" fill="var(--paper-white)"/>

      <path d="M380,0 L460,0 Q470,150 330,290 Q430,150 380,0 Z" fill="var(--ink)"/>
      <path d="M470,0 L560,0 L560,50 Q520,140 450,190 Q520,100 470,0 Z" fill="var(--ink)"/>

      <path class="photo" d="M0,0 L360,0 Q390,150 260,250 Q150,310 0,298 Z" fill="url(#barnTone)" role="img" aria-label="Photo of a red post frame home with a covered porch and landscaping"/>

      <path d="M0,520 Q360,490 560,290 L560,724 L0,724 Z" fill="var(--ink)"/>
      <path d="M0,506 Q360,476 552,276" fill="none" stroke="var(--ink)" stroke-width="1.2"/>

      <circle class="photo" cx="290" cy="790" r="220" fill="url(#interiorTone)" role="img" aria-label="Photo of a finished interior with timber beams and pendant lights"/>

      <circle cx="610" cy="690" r="150" fill="var(--paper-white)"/>
    </svg>
    <h1 class="about-title">About Company</h1>
    <p class="body-copy about-copy">Lorem Lorem ipsum dolor sit amet, consectetuer adipiscing elit, sed diam nonummy nibh euismod tincidunt ut laoreet dolore magna aliquam erat volutpat. Ut wisi enim ad minim veniam, quis</p>
    <p class="body-copy reverse-copy">Lorem Lorem ipsum dolor sit amet, consectetuer adipiscing elit, sed diam nonummy nibh euismod tincidunt ut laoreet dolore magna aliquam erat volutpat. Ut wisi enim ad minim veniam, quis nostrud exerci tation</p>
  </section>

</div>
</body>
</html>
```